Apartment Complex in Southeastern US needs new signage & identity!

Need a design for a physical sign/logo & signage for a 28 unit apartment complex in West Columbia, South Carolina, USA.

These are properties that, in their market , I would describe as "affordable." They are no-frills accommodations that are safe, clean and inexpensive.

The sign I want foremost is something that will be free-standing (not attached). Approximate measurements of the main finished sign should be about 4' x 6' (but really this is just an aspect ratio of course.)

Ideally also want to have smaller signs of a coordinated design created to denote the building number (maybe even on each door), but that is a secondary task. You'll get an idea for how ugly the current numbering and signage looks in some of the attached photos. Some of the photos also came from the old Chatterly page of the prior management company. (This project could also possibly expand into creating new assets for taking over and rebranding that chatterly page.)

The apartments are currently called "Brackwell Properties" but frankly speaking I despise this name and want to change (rebrand) it. As the new owner I am thinking to change the name:

Sign should basically say something like the following...

Hollin Apartments
1 & 2 Bedroom Units
3817 Dunmore Creek Rd.
Professionally Managed by
Ferrow Properties: (XXX)XXX-XXXX

"Managed by" part should be detachable. For instance if I ever need to change management companies, I'd just want to be able to swap out that part of the sign, not the whole thing, of course.

Another consideration is that it would be good if there could be a "units available" or "move-in-special" part that could be attached to the top based on the property's status.

I think that earth colors are favorable and nice looking for what this is and where it is located.... greens/browns/tans/greys, etc.

Many similar signs I've seen online and in person have an this Fair Tenancy Pledge logo on it (one of the example signs in the attached images appears this way). I may want to have that appear on the sign -- I'm not yet decided.

I'm attaching some logos of similar signs, as well as some photos of the property itself. You can probably also find more information and photos (Mapvista Road Lens.)

I can answer any question or inquiry you might have in pretty short time.

Target Market(s)

- Low-Mid income singles & families in the Southeast US looking for safe & affordable housing

Industry/Entity Type

Apartment

Requirements
Must have
• - A design proposal for an outdoor sign
• - Design for sign should have some 'detachable' parts for the management company, and to indicate whether units are available and
Nice to have
• - "Earthy" colors: tans/browns/greens etc. seem like it might be nice. (The region, [US postal code 28413] has lots and lots of pine trees.)
Should not have
• No comic sans! :)

```html
<!DOCTYPE html>
<html lang="en">
<head>
<meta charset="utf-8">
<title>Hollin Apartments – Entrance Sign</title>
<link rel="stylesheet" href="https://fonts.googleapis.com/css2?family=Cinzel:wght@500&family=Almendra&family=Arimo:wght@400;700&family=Libre+Baskerville:wght@400;700&display=swap">
<style>
  :root {
    --teal: #08705f;
    --brown: #8a5a2c;
    --tan: #a39480;
    --pine: #1c6b34;
    --panel-top: #ffffff;
    --panel-bottom: #cfe2c8;
    --olive: #86773a;
    --ink: #262626;
    --slate: #3c4a40;
    --wave-green: #2faa6c;
    --wave-brown: #a67c4e;
    --house: #b9c8c6;
  }
  * { margin: 0; padding: 0; box-sizing: border-box; }
  html, body { width: 1200px; height: 800px; overflow: hidden; background: #ffffff; }
  .sign { position: relative; width: 1200px; height: 800px; }
  .sign-frame { position: absolute; inset: 0; }
  .sign-text { position: absolute; left: 0; width: 1200px; text-align: center; white-space: nowrap; }
  .unit-types {
    top: 212px; left: 20px;
    font-family: "Cinzel", serif; font-weight: 500;
    font-size: 46px; letter-spacing: 5px; color: var(--slate);
  }
  .street-address {
    top: 296px; left: 0;
    font-family: "Almendra", serif; font-size: 36px; color: var(--olive);
  }
  .managed-label {
    top: 372px; left: 20px;
    font-family: "Arimo", sans-serif; font-size: 36px; color: var(--ink);
  }
  .manager-plate {
    position: absolute; left: 256px; top: 428px; width: 710px; height: 62px;
    border: 1px solid #8a8a8a; border-radius: 4px;
    background: linear-gradient(#fbfbfb, #d3d3d3 55%, #c4c4c4);
    box-shadow: 1px 2px 2px rgba(0,0,0,0.35);
    font-family: "Libre Baskerville", serif; font-size: 30px; letter-spacing: 1px;
    color: #333; display: flex; align-items: center; justify-content: center;
  }
  .availability-label {
    position: absolute; left: 880px; top: 498px; width: 160px; text-align: center;
    font-family: "Arimo", sans-serif; font-weight: 700; font-size: 18px; color: #111;
  }
  .availability-slot {
    position: absolute; left: 921px; top: 523px; width: 80px; height: 57px;
    background: #fff; border: 2px solid #222; border-radius: 5px;
    box-shadow: 1px 2px 2px rgba(0,0,0,0.4);
  }
  .accessibility-mark {
    position: absolute; left: 203px; top: 494px; width: 92px; height: 82px;
    background: #111; border-radius: 8px;
  }
  .postal-code {
    top: 543px; font-family: "Arimo", sans-serif; font-size: 36px; color: #222; left: 0;
    width: 1244px;
  }
  .city {
    top: 586px; font-family: "Arimo", sans-serif; font-size: 30px; color: #222; width: 1244px;
  }
  .complex-name {
    top: 630px; font-family: "Libre Baskerville", serif; font-weight: 700;
    font-size: 42px; color: var(--slate); width: 1250px;
  }
</style>
</head>
<body>
<div class="sign">
  <svg class="sign-frame" width="1200" height="800" viewBox="0 0 1200 800" aria-hidden="false">
    <defs>
      <linearGradient id="panelFill" x1="0" y1="0" x2="0" y2="1">
        <stop offset="0" stop-color="var(--panel-top)"/>
        <stop offset="1" stop-color="var(--panel-bottom)"/>
      </linearGradient>
      <linearGradient id="ovalFill" x1="0" y1="0" x2="0" y2="1">
        <stop offset="0" stop-color="#ffffff"/>
        <stop offset="1" stop-color="#d2d2d2"/>
      </linearGradient>
    </defs>

    <!-- lower base blocks -->
    <g class="base-block">
      <rect x="132" y="460" width="235" height="198" fill="#fff" stroke="var(--teal)" stroke-width="8"/>
      <rect x="150" y="480" width="215" height="158" fill="var(--tan)" stroke="var(--pine)" stroke-width="5"/>
      <rect x="865" y="462" width="250" height="196" fill="#fff" stroke="var(--teal)" stroke-width="8"/>
      <rect x="865" y="482" width="230" height="156" fill="var(--tan)" stroke="var(--pine)" stroke-width="5"/>
    </g>

    <!-- outer frame posts -->
    <g class="frame-outline" fill="#fff" stroke="var(--teal)" stroke-width="8">
      <path d="M168,152 L168,610 L185,610"/>
      <path d="M1075,152 L1075,610 L1055,610"/>
    </g>

    <!-- main panel -->
    <path class="main-panel" d="M185,285 L270,285 L270,160 Q620,80 995,155 L995,285 L1060,285 L1060,598 L185,598 Z"
          fill="url(#panelFill)" stroke="var(--brown)" stroke-width="8"/>
    <path d="M194,292 L194,590 L1052,590 L1052,292" fill="none" stroke="#8f8f8f" stroke-width="3"/>

    <!-- shoulders -->
    <rect x="182" y="268" width="92" height="30" rx="6" fill="#fff" stroke="var(--brown)" stroke-width="7"/>
    <rect x="962" y="268" width="100" height="30" rx="6" fill="#fff" stroke="var(--brown)" stroke-width="7"/>

    <!-- top arch -->
    <path class="top-arch" d="M118,205 Q620,0 1122,210" fill="none" stroke="var(--teal)" stroke-width="26" stroke-linecap="square"/>
    <path d="M122,204 Q620,0 1118,209" fill="none" stroke="#fff" stroke-width="13" stroke-linecap="square"/>

    <!-- vertical posts -->
    <rect x="238" y="168" width="20" height="105" fill="#fff" stroke="var(--teal)" stroke-width="6"/>
    <rect x="985" y="160" width="20" height="112" fill="#fff" stroke="var(--teal)" stroke-width="6"/>

    <!-- heading ornament band -->
    <rect x="465" y="155" width="255" height="16" fill="var(--wave-green)" role="img" aria-label="Green wave ornament"/>
    <rect x="535" y="177" width="252" height="15" fill="var(--wave-brown)" role="img" aria-label="Brown wave ornament"/>

    <!-- faint house backdrop -->
    <rect x="465" y="240" width="270" height="185" fill="var(--house)" opacity="0.28" role="img" aria-label="Faint outline of two houses behind the text"/>

    <!-- bottom oval -->
    <ellipse class="name-oval" cx="622" cy="612" rx="202" ry="94" fill="#fff" stroke="var(--teal)" stroke-width="12"/>
    <ellipse cx="622" cy="612" rx="184" ry="78" fill="url(#ovalFill)" stroke="var(--teal)" stroke-width="3"/>
  </svg>

  <div class="sign-text unit-types">1&amp;2 Bedroom Units</div>
  <div class="sign-text street-address">3817 Dunmore Creek Rd.</div>
  <div class="sign-text managed-label">Professionally Managed by:</div>
  <div class="manager-plate">Ferrow Properties: (xxx)xxx-xxxx</div>

  <div class="accessibility-mark" role="img" aria-label="Accessibility symbol"></div>
  <div class="availability-label">Available Ap.</div>
  <div class="availability-slot"></div>

  <div class="sign-text postal-code">28413</div>
  <div class="sign-text city">West Columbia SC</div>
  <div class="sign-text complex-name">Apartments</div>
</div>
</body>
</html>
```